・電子書籍の表紙デザインをお願いします。

・本の内容
モヤモヤグルグルしてるただの主婦でも、天職につながれば稼げるようになる。
自分の事を理解し天職につながることによって、
自信や人間関係やお金、仕事や健康までも、うまく回り始める。
私のエピソードから天職につながるプロセスを見てもらって解説してます。
後半で、あなたの天職につながるワークを実践して
スモールステップを踏み出せるようになるという内容になっています。

・デザイン要望
文字を大きく、パッと見て何が書いてあるかわかりやすいようにして欲しいです。

その他何かありましたら、気軽に質問して下さいね。
よろしくお願いいたします。

タイトルとして

スル~っととんとん拍子に
『ひらめく毎日!をひらく本』
モヤモヤグルグルしてたただの主婦の私が、
まさかの経営者になった理由
森川遥香

読者限定プレゼント
「何かしたい」でも「何をしたいのかわからない」
そんなあなたに
「星読みカルテ」プレゼント

入れて欲しいです。
とんとん拍子 → トントン拍子

軽快なイメージに一番近かったです。

皆さんのご提案、すべて素敵で迷いました。
ありがとうございました。

```html
<!DOCTYPE html>
<html lang="ja">
<head>
<meta charset="utf-8">
<title>ひらめく毎日!をひらく本</title>
<link rel="stylesheet" href="https://fonts.googleapis.com/css2?family=M+PLUS+Rounded+1c:wght@500;800;900&display=swap">
<style>
  :root {
    --paper: #fffdf2;
    --dot-field: #fff3b8;
    --ink: #1c1c1c;
    --title-red: #e5364f;
    --accent-pink: #f06b8e;
    --sky: #8dd3ea;
    --navy: #1d3766;
    --orange: #f29418;
    --white: #ffffff;
  }
  * { margin: 0; padding: 0; box-sizing: border-box; }
  html, body { width: 750px; height: 1200px; overflow: hidden; }
  body { font-family: "M PLUS Rounded 1c", sans-serif; background: var(--paper); }
  .cover {
    position: relative; width: 750px; height: 1200px; overflow: hidden;
    background: radial-gradient(circle at 50% 35%, var(--paper) 0%, var(--dot-field) 100%);
  }
  .lead-arrows { position: absolute; left: 0; top: 30px; }
  .lead {
    position: absolute; left: 0; width: 750px; top: 72px; white-space: nowrap;
    text-align: center; font-weight: 900; font-size: 50px; color: var(--ink);
  }
  .title {
    position: absolute; left: 0; width: 750px; text-align: center;
    font-weight: 900; line-height: 1; white-space: nowrap; display: block;
  }
  .title-main { top: 185px; color: var(--title-red); font-size: 92px; letter-spacing: -2px; }
  .title-main .particle {
    display: inline-block; font-size: 34px; color: var(--ink); letter-spacing: 0;
    width: 50px; height: 50px; line-height: 48px; border-radius: 50%;
    background: var(--white); vertical-align: bottom; margin-left: 6px;
  }
  .title-sub { top: 315px; color: var(--ink); font-size: 100px; letter-spacing: 6px; }
  .author {
    position: absolute; left: 410px; top: 468px; white-space: nowrap;
    font-weight: 800; font-size: 42px; letter-spacing: 8px; color: var(--ink);
  }
  .ground { position: absolute; left: 0; top: 820px; }
  .illustration-hero {
    position: absolute; left: 40px; top: 420px; width: 320px; height: 450px;
    border-radius: 45% 50% 40% 45%;
    background: linear-gradient(160deg, #ffe08a 0%, #bfe6a8 55%, #f7f7f7 100%);
  }
  .gift { position: absolute; left: 468px; top: 620px; width: 266px; z-index: 2; }
  .gift-label {
    position: relative; z-index: 1; margin: 0 auto -14px; width: 230px;
    background: var(--accent-pink); color: var(--white); text-align: center;
    font-weight: 800; font-size: 20px; padding: 5px 0; border-radius: 6px;
  }
  .gift-box {
    background: var(--white); border: 4px solid var(--accent-pink); border-radius: 10px;
    padding: 20px 8px 10px; text-align: center; font-weight: 800; font-size: 18px; line-height: 1.35; color: var(--ink);
  }
  .gift-name {
    display: inline-block; margin: 2px 0; color: var(--title-red); font-size: 24px;
    border-bottom: 3px solid var(--accent-pink);
  }
  .illustration-mini {
    position: absolute; left: 652px; top: 826px; width: 76px; height: 68px;
    border-radius: 45%; background: linear-gradient(180deg, #ffe08a, #f7c9a0); z-index: 1;
  }
  .surprise {
    position: absolute; left: 140px; top: 925px; writing-mode: vertical-rl;
    font-weight: 900; font-size: 30px; color: var(--navy); transform: rotate(-14deg);
  }
  .story-line {
    position: absolute; left: 222px; white-space: nowrap;
    font-weight: 900; color: var(--navy); font-size: 45px; line-height: 1;
  }
  .story-line.first { top: 905px; }
  .story-line.second { top: 970px; }
  .story-key {
    position: absolute; left: 188px; top: 1040px; white-space: nowrap;
    padding: 8px 22px; background: var(--white); border-radius: 40px;
    font-weight: 900; color: var(--orange); font-size: 54px; line-height: 1.1;
  }
</style>
</head>
<body>
<main class="cover">
  <svg class="lead-arrows" width="750" height="50" viewBox="0 0 750 50" aria-hidden="true">
    <g fill="none" stroke="var(--accent-pink)" stroke-width="5" stroke-linecap="round" stroke-linejoin="round">
      <path d="M130 42 Q170 10 230 22"/><path d="M218 12 L232 22 L218 32"/>
      <path d="M470 44 L490 14 L610 14"/><path d="M598 4 L612 14 L598 24"/>
    </g>
  </svg>
  <p class="lead">スル〜っと トントン拍子に</p>

  <h1>
    <span class="title title-main">ひらめく毎日!<span class="particle">を</span></span>
    <span class="title title-sub">ひらく本</span>
  </h1>

  <p class="author">森川 遥香</p>

  <svg class="ground" width="750" height="380" viewBox="0 0 750 380" aria-hidden="true">
    <path d="M0 50 Q375 -30 750 50 L750 380 L0 380 Z" fill="var(--sky)"/>
  </svg>

  <div class="illustration-hero" role="img" aria-label="イラスト：元気に跳ねる女性"></div>

  <section class="gift">
    <p class="gift-label">読者限定プレゼント</p>
    <div class="gift-box">
      「何かしたい」でも<br>「何をしたいのかわから<br>ない」そんなあなたに<br>
      <span class="gift-name">「星読みカルテ」</span><br>プレゼント!
    </div>
  </section>

  <div class="illustration-mini" role="img" aria-label="イラスト：悩む女性"></div>

  <p class="surprise">まさかの</p>
  <p class="story-line first">モヤモヤグルグルしてた</p>
  <p class="story-line second">ただの主婦の私が、</p>
  <p class="story-key">経営者になった理由</p>
</main>
</body>
</html>
```